Flyer Design Print Ad for Clothing Store

We are a modest women's clothing store. We are looking for a print ad 90*134 mm that is attention grabbing and can serve as a template for us going forward. We cannot use pictures of actual women. We need it to include our logo, store hours, physical address, website, phone number. We would use this template and change the call to action as necessary e. g. BOGO Sale, 30% off, flash sale, summer sale etc. Our colors are black and white and our fonts are Bodoni sans and Athens.

Target Market(s)

Women from teen to age 70

Industry/Entity Type

Women's clothing

Font styles to use
Other font styles liked:
• Athens, Bodoni Sans

Requirements
Must have
• Our, logo, phone number, website, address and store hours
Nice to have
• I'd like something that's not just our flat logo but something that will make someone pause to look
Should not have
• Pictures of women

```html
<!DOCTYPE html>
<html lang="en">
<head>
<meta charset="utf-8">
<title>Alderwick – BOGO Sale Flyer</title>
<link rel="stylesheet" href="https://fonts.googleapis.com/css2?family=Bodoni+Moda:wght@400;500;700;800&family=Frank+Ruhl+Libre:wght@400;500&display=swap">
<style>
  :root {
    --backdrop: #e8e4e4;
    --paper: #f7f6f6;
    --ink: #0b0b0b;
    --white: #ffffff;
    --rose: #e08d91;
    --serif: "Bodoni Moda", "Bodoni 72", serif;
    --hebrew: "Frank Ruhl Libre", serif;
  }
  * { margin: 0; padding: 0; box-sizing: border-box; }
  html, body { width: 960px; height: 1200px; overflow: hidden; background: var(--backdrop); }
  .flyer {
    position: absolute; left: 77px; top: 0; width: 806px; height: 1200px;
    background: var(--paper); overflow: hidden; color: var(--ink); font-family: var(--serif);
  }
  .pattern-field {
    position: absolute; inset: 0;
    background: radial-gradient(circle at 50% 50%, #f9f8f8 0%, #efeded 100%);
  }
  .frame { position: absolute; border: 2px solid var(--ink); }
  .frame--outer { left: 24px; top: 24px; right: 23px; bottom: 25px; }
  .frame--inner { left: 39px; top: 38px; right: 38px; bottom: 40px; }
  .brand-mark {
    position: absolute; left: 307px; top: 65px; width: 180px; height: 180px;
    border-radius: 50%; background: var(--ink);
  }
  .brand-name {
    position: absolute; left: 0; right: 0; top: 276px; text-align: center;
    font-size: 46px; font-weight: 500; letter-spacing: 14px; line-height: 1; padding-left: 14px;
  }
  .tag {
    position: absolute; display: flex; align-items: center; justify-content: center;
    color: var(--white); font-family: var(--serif); line-height: 1; overflow: hidden;
  }
  .tag span { display: block; line-height: 0.8; }
  .tag--bogo {
    left: 112px; top: 396px; width: 482px; height: 158px; background: var(--ink);
    transform: rotate(-8deg); font-size: 136px; font-weight: 700; letter-spacing: -2px;
  }
  .tag--bogo span { transform: translateY(6px); }
  .tag--sale {
    left: 232px; top: 548px; width: 443px; height: 131px; background: var(--rose);
    transform: rotate(-10.5deg); font-size: 132px; font-weight: 500;
    box-shadow: 2px 6px 10px rgba(0,0,0,0.25);
  }
  .tag--sale span { transform: translateY(6px); }
  .line { position: absolute; left: 0; right: 0; text-align: center; line-height: 1; white-space: nowrap; }
  .hours { font-size: 27px; }
  .hours--en { top: 718px; }
  .hours--he { top: 747px; }
  .address { font-size: 29px; font-weight: 700; }
  .address--center { top: 791px; }
  .address--city { top: 830px; }
  .divider { position: absolute; left: 371px; top: 880px; width: 65px; height: 2px; background: var(--ink); }
  .directions { font-size: 26px; }
  .he { font-family: var(--hebrew); font-size: 24px; direction: rtl; }
  .dir-1 { top: 906px; }
  .dir-2 { top: 940px; }
  .dir-3 { top: 977px; }
  .dir-4 { top: 1012px; }
  .buses { top: 1044px; font-size: 16px; letter-spacing: 0.5px; }
  .contact-band {
    position: absolute; left: 0; right: 0; top: 1091px; height: 44px; background: var(--ink);
    color: var(--white); display: flex; align-items: center; justify-content: center; gap: 20px;
    font-size: 25px; font-weight: 700; letter-spacing: 6px;
  }
  .contact-item { display: flex; align-items: center; gap: 12px; }
  .contact-item svg { width: 26px; height: 26px; }
</style>
</head>
<body>
  <main class="flyer">
    <div class="pattern-field" role="img" aria-label="Soft repeating floral ornament pattern in pale grey on white"></div>
    <div class="frame frame--outer"></div>
    <div class="frame frame--inner"></div>

    <div class="brand-mark"></div>
    <div class="brand-name">ALDERWICK</div>

    <div class="tag tag--bogo"><span>BOGO</span></div>
    <div class="tag tag--sale"><span>SALE</span></div>

    <div class="line hours hours--en">S-TH- 10:30-12:30</div>
    <div class="line hours hours--he"><span dir="rtl" style="font-family:var(--hebrew)">א-ה</span> 20:30 - 22:30</div>

    <div class="line address address--center">CEDAR COURT SHOPPING CENTER</div>
    <div class="line address address--city">GIVAT OREN, JERUSALEM, ISRAEL</div>

    <div class="divider"></div>

    <div class="line he dir-1">מרכז מסחרי גבעת אורן</div>
    <div class="line directions dir-2">Hillview Shopping Center</div>
    <div class="line he dir-3">(מעל הקפה הפינתי)</div>
    <div class="line he dir-4">ניתן להגיע גם משדרות אורן 1</div>
    <div class="line buses">Buses 21, 22, 39, 41, 45, 52, 59, 65, 68, 69, 77</div>

    <div class="contact-band">
      <div class="contact-item">
        <svg viewBox="0 0 24 24" fill="none" stroke="currentColor" stroke-width="1.4" stroke-linejoin="round">
          <path d="M5 3.5l3 .2 1.6 4-2 1.5a11 11 0 0 0 6.2 6.2l1.5-2 4 1.6.2 3a2 2 0 0 1-2.2 2A16 16 0 0 1 3 5.7a2 2 0 0 1 2-2.2z"/>
          <path d="M14 3.5a6.5 6.5 0 0 1 6.5 6.5M14 6.5a3.5 3.5 0 0 1 3.5 3.5"/>
        </svg>
        <span>077-5550142</span>
      </div>
      <div class="contact-item">
        <svg viewBox="0 0 24 24" fill="none" stroke="currentColor" stroke-width="1.6">
          <circle cx="12" cy="12" r="9.5"/>
          <ellipse cx="12" cy="12" rx="4" ry="9.5"/>
          <path d="M2.5 12h19"/>
        </svg>
        <span>ALDERWICK.CO.IL</span>
      </div>
    </div>
  </main>
</body>
</html>
```